Point of Sale Systems Web Design Project

I need a complete redesign of my existing website. I sell point of sale systems and need to seamlessly combine the features, products and services of several companies I represent. The current site is at www.tillgroveplaza.com. The new site will be rebranded as www.TradeZoral.com. I will be adding products from www.quaylinkpro.com, www.pinrowly.com, www.dakswivo.com as well as other similar products and services such as http://kelbafund.com/homepage_USA.html

The new tag line will be:
Electronic Payment Systems Made ZORAL!
Updates

I have made a change to the website name. The new name will be TradeZoral.com. I look forward to seeing the designs. Please see http://www.zoral.com.au/index.html for the inspiration behind the new name. I am also going to increase the budget for this project. Thank you

Target Market(s)

These are products and services for business owners. We provide Credit Card Processing Equipment and Processing Services to Retail, Restaurant, Home-based, and Internet businesses.

Industry/Entity Type

Electronic

Requirements
Must have
• Visitors need to be able to view video demos and download PDF documents. Site should be easy to update with new products or services.
Nice to have
• Designs I like: http://www.thebrivelworks.com, http://www.plantyourbalconies.com, http://www.qortalvistagroup.com/

```html
<!DOCTYPE html>
<html lang="en">
<head>
<meta charset="utf-8">
<title>TradeZoral — POS Technology, Systems and Solutions</title>
<link rel="stylesheet" href="https://fonts.googleapis.com/css2?family=Arimo:wght@400&family=Ubuntu:wght@400;500;700&family=Open+Sans:ital,wght@0,400;0,600;1,400&display=swap">
<style>
:root{
  --white:#ffffff;
  --ink:#1e1e1e;
  --text:#333333;
  --muted:#777777;
  --sky:#2aa3e6;
  --sky-deep:#1577c2;
  --nav-top:#4fb8ee;
  --nav-bottom:#1b86cf;
  --nav-active:#9be58f;
  --hero-top:#1c1d1f;
  --hero-bottom:#3b3f43;
  --hero-title:#3fb0ec;
  --hero-text:#e4e4e4;
  --rule:#d9d9d9;
  --panel:#f4f4f4;
  --lime:#7cbb2a;
  --slate:#8a8a8a;
  --azure:#2590da;
  --pill:#3a3a3a;
  --field:#ececec;
  --field-line:#c9c9c9;
  --row:#e9e9e9;
  --orange:#d46d00;
  --footer-top:#3a3a3a;
  --footer-bottom:#141414;
}
*{margin:0;padding:0;box-sizing:border-box}
html,body{width:794px;height:1200px;overflow:hidden;background:var(--white)}
body{position:relative;font-family:"Open Sans",Arial,sans-serif;color:var(--text)}
.abs{position:absolute}

/* header */
.brand{left:10px;top:34px;display:flex;align-items:center;gap:8px}
.brand-mark{width:36px;height:36px;background:var(--sky)}
.brand-name{font-family:"Ubuntu",sans-serif;font-weight:700;font-size:25px;color:var(--sky-deep);line-height:1}
.brand-tag{left:54px;top:63px;font-family:"Ubuntu",sans-serif;font-size:9.5px;color:#243a63;font-weight:500}
.main-nav{left:250px;top:22px;width:524px;height:72px;border-radius:5px;
  background:linear-gradient(var(--nav-top),var(--nav-bottom));display:flex;box-shadow:0 2px 4px rgba(0,0,0,.25)}
.main-nav a{flex:1;text-decoration:none;color:var(--white);font-family:"Ubuntu",sans-serif;font-size:11.5px;
  text-align:center;padding-top:15px;border-right:1px solid rgba(255,255,255,.35);position:relative}
.main-nav a:last-child{border-right:0}
.main-nav a.active{color:var(--nav-active)}
.main-nav svg{position:absolute;left:50%;top:42px;transform:translateX(-50%)}

.band-light{left:0;top:120px;width:794px;height:8px;background:var(--rule)}

/* hero */
.hero{left:0;top:128px;width:794px;height:237px;background:linear-gradient(var(--hero-top),var(--hero-bottom))}
.hero-title{left:38px;top:167px;font-family:"Ubuntu",sans-serif;font-size:22px;color:var(--hero-title);font-weight:400}
.hero-rule{left:38px;top:203px;width:404px;height:1px;background:#5a5d60}
.hero-copy{left:38px;top:209px;font-family:"Arimo",Arial,sans-serif;font-size:9.9px;line-height:18px;color:var(--hero-text)}
.hero-copy span{display:block;white-space:nowrap}
.btn-read{left:37px;top:309px;width:70px;height:23px;background:#55585b;color:#e8e8e8;font-family:"Ubuntu",sans-serif;
  font-size:11px;line-height:23px;text-align:center;border:1px solid #6a6d70}
.hero-visual{left:505px;top:146px;width:240px;height:190px;border-radius:8px;
  background:linear-gradient(#6f93ba,#2f5f95 55%,#5a6066 85%,#8d9195)}

.band-mid{left:0;top:365px;width:794px;height:7px;background:#e6e6e6}

/* products */
.products{left:0;top:372px;width:794px;height:228px;background:var(--panel)}
.product-title{font-style:italic;font-size:18px;font-weight:400}
.product-photo{height:98px;border-radius:14px}
.product-text{font-size:10.5px;line-height:14px;color:var(--text);width:225px}
.pill{height:18px;border-radius:9px;background:linear-gradient(#5a5a5a,#1f1f1f);color:var(--white);font-size:10px;
  line-height:18px;text-align:center;font-style:italic}

/* about */
.about{left:0;top:600px;width:794px;height:243px;background:linear-gradient(#d6d6d6,#f5f5f5 60%)}
.section-title{font-style:italic;font-size:18px;color:var(--ink);font-weight:400}
.about-copy{left:18px;width:478px;font-size:9.6px;line-height:21.5px;color:var(--ink)}
.video-frame{left:504px;top:645px;width:275px;height:186px;border-radius:6px;background:#1a1a1a}
.video-screen{left:511px;top:652px;width:261px;height:157px;background:linear-gradient(120deg,#c23a35,#e7d0c4 45%,#4c86c2)}
.video-bar{left:511px;top:812px;width:261px;height:12px}

/* lower */
.lower{left:0;top:843px;width:794px;height:309px;background:#f7f7f7}
.form-label{left:23px;font-size:10px;color:var(--text)}
.form-colon{left:137px;font-size:10px}
.field{left:148px;width:192px;height:20px;background:var(--field);border:1px solid var(--field-line)}
.feature-thumb{border-radius:2px}
.feature-text{left:425px;width:150px;font-size:7.8px;line-height:14px;color:var(--text)}
.learn{font-size:7.8px;color:var(--ink)}
.social-row{left:600px;width:175px;height:41px;background:var(--row);display:flex;align-items:center;font-size:10.5px;color:var(--ink)}
.social-row i{width:28px;height:28px;border-radius:50%;background:radial-gradient(circle at 40% 35%,#8fd2f7,#1e7fc4);margin:0 14px 0 9px;display:inline-block}
.call-box{left:602px;top:1030px;width:173px;height:56px;border:1px solid #8fb3cf;border-radius:5px;background:linear-gradient(#ffffff,#dcebf6);text-align:center}
.call-label{font-size:16px;color:var(--orange);margin-top:5px;display:flex;justify-content:center;align-items:center;gap:6px}
.call-number{font-size:18px;color:var(--ink);margin-top:1px}
.partner-badge{left:635px;top:1102px;width:97px;height:28px;border-radius:4px;background:#e2e2e2}

.footer{left:0;top:1152px;width:794px;height:48px;background:linear-gradient(var(--footer-top),var(--footer-bottom))}
.footer p{text-align:center;font-size:8.5px;color:#d6d6d6;margin-top:17px}
</style>
</head>
<body>

<header>
  <div class="abs brand"><span class="brand-mark"></span><span class="brand-name">TradeZoral</span></div>
  <div class="abs brand-tag">Electronic Payment Systems Made ZORAL!</div>
  <nav class="abs main-nav">
    <a href="#" class="active">Home
      <svg width="22" height="20" viewBox="0 0 22 20"><path d="M2 10 11 2l9 8" fill="none" stroke="#fff" stroke-width="2"/><rect x="5" y="9" width="12" height="10" fill="#fff"/><rect x="9" y="13" width="4" height="6" fill="#2a8dd0"/></svg></a>
    <a href="#">Products
      <svg width="20" height="20" viewBox="0 0 20 20"><rect x="2" y="3" width="16" height="15" fill="#8b1e1e"/><rect x="2" y="3" width="16" height="4" fill="#c23a3a"/></svg></a>
    <a href="#">Solutions
      <svg width="20" height="20" viewBox="0 0 20 20"><circle cx="10" cy="10" r="8" fill="#3a7ad0"/><path d="M10 10V2a8 8 0 0 1 8 8z" fill="#f2c200"/><path d="M10 10h8a8 8 0 0 1-6 7.7z" fill="#e04a2a"/></svg></a>
    <a href="#">Services
      <svg width="20" height="20" viewBox="0 0 20 20"><circle cx="10" cy="10" r="8" fill="#dfe8f0" stroke="#5d7f9c" stroke-width="2" stroke-dasharray="3 2"/><circle cx="10" cy="10" r="3.5" fill="#2f6fb0"/></svg></a>
    <a href="#">Contact&nbsp; Us
      <svg width="22" height="22" viewBox="0 0 22 22"><circle cx="11" cy="11" r="10" fill="#f2c230"/><path d="M7 6c1 0 2 2 2 3s-1 1-1 2 2 3 3 3 1-1 2-1 3 1 3 2-1 2-2 2c-4 0-8-5-8-9 0-1 0-2 1-2z" fill="#fff"/></svg></a>
  </nav>
</header>

<div class="abs band-light"></div>

<section class="abs hero"></section>
<h1 class="abs hero-title">POS Technology, Systems and Solutions</h1>
<div class="abs hero-rule"></div>
<p class="abs hero-copy">
  <span>The standard chunk of Lorem Ipsum used since the 1500s is reproduced below for those interested.</span>
  <span>Sections 1.10.32 and 1.10.33 from "de Finibus Bonorum et Malorum" by Cicero are also reproduced</span>
  <span>in their exact original form, accompanied by English versions from the 1914 translation by H. Rack-</span>
  <span>ham. Many desktop publishing packages and web page editors now use Lorem Ipsum as their default</span>
  <span>model text, and a search for 'lorem ipsum' will uncover many web sites still in their infancy.</span>
</p>
<a class="abs btn-read">Read more</a>
<svg class="abs" style="left:478px;top:203px" width="22" height="22" viewBox="0 0 22 22"><circle cx="11" cy="11" r="10" fill="#0d0d0d" stroke="#777"/><path d="M13 6 8 11l5 5" fill="none" stroke="#fff" stroke-width="2.4"/></svg>
<svg class="abs" style="left:751px;top:203px" width="22" height="22" viewBox="0 0 22 22"><circle cx="11" cy="11" r="10" fill="#0d0d0d" stroke="#777"/><path d="M9 6l5 5-5 5" fill="none" stroke="#fff" stroke-width="2.4"/></svg>
<div class="abs hero-visual" role="img" aria-label="Photo of a point of sale touch-screen terminal showing a register interface"></div>

<div class="abs band-mid"></div>

<section class="abs products"></section>
<h2 class="abs product-title" style="left:33px;top:388px;color:var(--lime)">Dakswivo</h2>
<div class="abs product-photo" style="left:18px;top:421px;width:238px;background:linear-gradient(110deg,#1d2b45,#7d8ea6 50%,#d8dee6)" role="img" aria-label="Hand holding a smartphone with a card reader attached"></div>
<p class="abs product-text" style="left:23px;top:528px">Lorem Ipsum is simply dummy text of the printing and typesetting industry.</p>
<a class="abs pill" style="left:197px;top:555px;width:56px">more</a>

<h2 class="abs product-title" style="left:354px;top:388px;color:var(--slate)">Quaylink Pro</h2>
<div class="abs product-photo" style="left:282px;top:421px;width:238px;background:linear-gradient(110deg,#2a2f35,#6d5a48 50%,#d6b28e)" role="img" aria-label="Woman using a touch-screen point of sale terminal"></div>
<p class="abs product-text" style="left:292px;top:528px">Lorem Ipsum is simply dummy text of the printing and typesetting industry.</p>
<a class="abs pill" style="left:468px;top:555px;width:55px">more</a>

<h2 class="abs product-title" style="left:585px;top:388px;color:var(--azure)">Pinrowly Salon</h2>
<div class="abs product-photo" style="left:541px;top:421px;width:238px;background:linear-gradient(110deg,#6e2a45,#b77a8c 45%,#e9d8dc)" role="img" aria-label="Portrait of a woman with a styled red haircut"></div>
<p class="abs product-text" style="left:556px;top:528px">Lorem Ipsum is simply dummy text of the printing and typesetting industry.</p>
<a class="abs pill" style="left:723px;top:555px;width:55px">more</a>

<section class="abs about"></section>
<h2 class="abs section-title" style="left:18px;top:616px">About Us</h2>
<p class="abs about-copy" style="top:645px">Lorem Ipsum is simply dummy text of the printing and typesetting industry. Lorem Ipsum has been the industry's standard dummy text ever since the 1500s, when an unknown printer took a galley of type and scrambled it to make a type specimen book. It has survived not only five centuries, but also the leap into electronic typesetting, remaining essentially unchanged</p>
<p class="abs about-copy" style="top:734px;left:24px;width:472px">Lorem Ipsum is simply dummy text of the printing and typesetting industry. Lorem Ipsum has been the industry's standard dummy text ever since the 1500s, when an unknown printer took a galley of type and scrambled it to make a type specimen book. It has survived not only five centuries, but also the leap into electronic typesetting, remaining essentially unchanged</p>
<h2 class="abs section-title" style="left:505px;top:616px">Video Demos</h2>
<div class="abs video-frame"></div>
<div class="abs video-screen" role="img" aria-label="Video demo still of a woman presenting a touch-screen terminal"></div>
<svg class="abs" style="left:620px;top:716px" width="30" height="30" viewBox="0 0 30 30"><circle cx="15" cy="15" r="14" fill="rgba(0,0,0,.45)"/><path d="M11 8l11 7-11 7z" fill="#6fbf2a"/></svg>
<svg class="abs video-bar" viewBox="0 0 261 12"><rect x="0" y="5" width="220" height="2" fill="#444"/><rect x="0" y="5" width="22" height="2" fill="#7cbb2a"/><circle cx="236" cy="6" r="5" fill="#333"/><path d="M234 3.5l4 2.5-4 2.5z" fill="#aaa"/><circle cx="250" cy="6" r="5" fill="#333"/><rect x="247.5" y="3.5" width="1.6" height="5" fill="#aaa"/><rect x="250.9" y="3.5" width="1.6" height="5" fill="#aaa"/></svg>

<section class="abs lower"></section>
<h2 class="abs section-title" style="left:16px;top:860px">Quick Contact</h2>
<form>
  <label class="abs form-label" style="top:915px">Full name</label><span class="abs form-colon" style="top:915px">:</span><span class="abs field" style="top:911px"></span>
  <label class="abs form-label" style="top:945px">Email</label><span class="abs form-colon" style="top:945px">:</span><span class="abs field" style="top:941px"></span>
  <label class="abs form-label" style="top:975px">Phone</label><span class="abs form-colon" style="top:975px">:</span><span class="abs field" style="top:971px"></span>
  <label class="abs form-label" style="top:1006px">Type of inquires</label><span class="abs form-colon" style="top:1006px">:</span><span class="abs field" style="top:1001px"></span>
  <label class="abs form-label" style="top:1036px">Additional Information</label><span class="abs form-colon" style="top:1036px">:</span><span class="abs field" style="top:1032px;height:66px"></span>
  <span class="abs pill" style="left:216px;top:1107px;width:51px;font-style:normal">Submit</span>
</form>

<h2 class="abs section-title" style="left:369px;top:867px">Featured Items</h2>
<div class="abs feature-thumb" style="left:365px;top:919px;width:49px;height:33px;background:linear-gradient(#b0303a,#7a1a22)" role="img" aria-label="Gift card"></div>
<p class="abs feature-text" style="top:916px">Lorem ipsum dolor sit amet, consectetur adipisicing elit, sed do eiusmod tempor incididunt ut labore.</p>
<span class="abs learn" style="left:521px;top:966px">Learn more</span>
<div class="abs feature-thumb" style="left:366px;top:988px;width:40px;height:50px;background:linear-gradient(#7b8a5a,#c9cfc3)" role="img" aria-label="Bucket of banknotes"></div>
<p class="abs feature-text" style="top:986px">Lorem ipsum dolor sit amet, consectetur adipisicing elit, sed do eiusmod tempor incididunt ut labore.</p>
<span class="abs learn" style="left:521px;top:1037px">Learn more</span>

<h2 class="abs section-title" style="left:613px;top:861px">Connect With Us</h2>
<div class="abs social-row" style="top:902px"><i></i>connect with Friendlo</div>
<div class="abs social-row" style="top:944px"><i></i>follow us Chirpel</div>
<div class="abs social-row" style="top:986px"><i></i>Email Share</div>
<svg class="abs" style="left:616px;top:1000px" width="16" height="12" viewBox="0 0 16 12"><rect x="0.5" y="0.5" width="15" height="11" fill="#fff"/><path d="M1 1l7 6 7-6" fill="none" stroke="#1e7fc4"/></svg>
<div class="abs call-box">
  <div class="call-label"><svg width="20" height="16" viewBox="0 0 20 16"><rect x="1" y="4" width="18" height="11" rx="2" fill="#d46d00"/><path d="M5 4a5 3 0 0 1 10 0" fill="none" stroke="#d46d00" stroke-width="3"/></svg>Call Us</div>
  <div class="call-number">888-555-0142</div>
</div>
<div class="abs partner-badge"></div>

<footer class="abs footer"><p>Copyright (c) 2011. www.tillgroveplaza.com</p></footer>

</body>
</html>
```